TOLO Electrical Services Letter Head

I need a professional clean looking design that will incorporate my company logo and information such as postal address, website, contact email "service@tolovoltworks.com.au" and phone number.

somewhere on the document i will also require my electrical contractor number "EC 046215" and my Australian Business number "57 139 604 282" these have to legally be on the document so they dont need to be a main feature, maybe in the footer in a smaller text.

Can you also have the 3 blue dashes from my logo as the watermark.

I would like the colour scheme to match my logo, business card and website www.tolovoltworks.com.au

I have the JPEG and PNG files for my logo which it will not allow me to upload as they are too wide, if you require these please let me know.

Target Market(s)

To be used for quotes and letters to commercial clients

Industry/Entity Type

Electric Company

Colors
0555a3
3176b5
85acd3
cfdfed
eaf1f7

Requirements
Must have
• company logo and information such as postal address, website, contact email "service@tolovoltworks.com.au" and phone number.
• somewhere on the document i will also require my electrical contractor number "EC 046215" and my Australian Business number "57 139 604 282" these have to legally be on the document so they dont need to be a main feature, maybe in the footer in a smaller text.
• I would like the colour scheme to match my logo, business card and website www.tolovoltworks.com.au
Nice to have
• Can you also have the 3 blue dashes from my logo as the watermark.

```html
<!DOCTYPE html>
<html lang="en">
<head>
<meta charset="utf-8">
<title>TOLO Electrical Services Letterhead</title>
<link rel="stylesheet" href="https://fonts.googleapis.com/css2?family=Arimo:wght@400;700&family=Tinos:wght@400&display=swap">
<style>
  :root {
    --blue-deep: #0555a3;
    --blue-mid: #3176b5;
    --blue-soft: #85acd3;
    --blue-pale: #cfdfed;
    --blue-mist: #eaf1f7;
    --backdrop: #ddd0b8;
    --paper: #ffffff;
    --ink: #2b2b2b;
    --ink-soft: #555555;
  }
  * { box-sizing: border-box; margin: 0; padding: 0; }
  html, body {
    width: 1200px; height: 900px; overflow: hidden;
    background: var(--backdrop);
  }
  .letterhead {
    position: absolute; left: 300px; top: 25px;
    width: 600px; height: 849px;
    background: var(--paper);
    box-shadow: 0 6px 24px rgba(0,0,0,.12);
    overflow: hidden;
  }
  .letterhead__art { position: absolute; inset: 0; }
  .brand {
    position: absolute; left: 28px; top: 96px;
    display: flex; align-items: center; gap: 6px;
    font-family: "Arimo", Arial, sans-serif; font-weight: 700;
    font-size: 15px; color: var(--ink); letter-spacing: .2px;
  }
  .brand__mark { width: 12px; height: 12px; background: var(--blue-mid); }
  .legal {
    position: absolute; left: 28px; top: 116px;
    font-family: "Tinos", "Times New Roman", serif; font-size: 12px;
    line-height: 13px; color: var(--ink);
  }
  .letter-body {
    position: absolute; left: 108px; top: 262px; width: 408px;
    font-family: "Arimo", Arial, sans-serif; font-size: 8.4px;
    line-height: 13.6px; color: var(--ink-soft); text-align: justify;
  }
  .letter-body p + p { margin-top: 13px; }
  .sign-off {
    position: absolute; left: 448px; top: 478px;
    font-family: "Arimo", Arial, sans-serif; font-size: 8.4px; color: var(--ink-soft);
  }
  .signature {
    position: absolute; left: 440px; top: 494px; width: 70px; height: 26px;
    background: linear-gradient(90deg, rgba(30,30,30,.0), rgba(30,30,30,.35), rgba(30,30,30,.0));
    border-radius: 12px;
  }
  .seal {
    position: absolute; left: 430px; top: 500px; width: 52px; height: 52px;
    border: 2px solid var(--blue-soft); border-radius: 50%;
  }
  .footer {
    position: absolute; right: 74px; top: 760px; text-align: right;
    font-family: "Tinos", "Times New Roman", serif; font-size: 11.5px;
    line-height: 12px; color: var(--ink);
  }
</style>
</head>
<body>
  <main class="letterhead">
    <svg class="letterhead__art" viewBox="0 0 600 849" width="600" height="849" aria-hidden="true">
      <path fill="var(--blue-mid)" d="M0,0 H600 V6 C470,14 360,30 250,44 C160,54 80,58 0,52 Z"/>
      <path fill="var(--blue-deep)" d="M0,10 C110,30 230,32 340,22 C430,14 520,6 600,0 V4 C500,20 400,40 290,56 C190,70 90,80 0,82 Z"/>
      <path fill="none" stroke="var(--paper)" stroke-width="3" d="M0,14 C140,36 300,30 440,14 C500,8 560,4 600,2"/>
      <path fill="var(--blue-mid)" d="M600,22 C572,140 556,300 560,430 C563,520 585,590 600,620 Z"/>
      <path fill="var(--blue-deep)" d="M600,60 C582,180 574,320 580,440 C584,530 594,590 600,610 Z"/>
      <path fill="none" stroke="var(--blue-soft)" stroke-width="2" d="M600,30 C578,150 563,300 567,430 C570,520 588,585 600,614"/>
    </svg>

    <div class="brand"><span class="brand__mark"></span>TOLO Electrical Services</div>
    <div class="legal">Aus Business # 57 139 604 282<br>EC 046215</div>

    <div class="letter-body">
      <p>Lorem ipsum dolor sit amet, consectetur adipiscing elit. Donec orci purus, luctus vitae dignissim eu, iaculis sed purus. Vivamus faucibus, ipsum nec aliquet viverra, leo mauris condimentum ligula, sit amet sagittis enim ligula quis arcu. Nam egestas tortor id nisi porttitor mattis. In tortor ante, ultricies in suscipit a, tempus non massa. Vivamus et auctor mi. Fusce vel massa nulla. Phasellus nec eros mauris, et scelerisque orci.</p>
      <p>Donec malesuada orci vitae nulla accumsan porta a id massa. Quisque accumsan iaculis magna sit amet fringilla. Maecenas consequat, magna eget tincidunt semper, odio nibh rutrum mi, id feugiat ante nisi eu risus. Vestibulum nunc orci, rhoncus a placerat in, ultricies in mi. Cras mattis varius eros, vel fringilla nisi suscipit eget. Quisque scelerisque sagittis nulla at porttitor.</p>
      <p>Sed id augue vitae urna euismod commodo aliquet a quam. Pellentesque arcu velit, cursus et malesuada ut, consequat et diam. Nullam erat sem, rhoncus id ullamcorper vitae, rhoncus et arcu. In ultricies ultricies nulla, ut rutrum nisi iaculis at. Donec eu magna a metus ornare faucibus. Fusce aliquet faucibus ultricies. Morbi semper, est id tincidunt gravida, sem arcu adipiscing lacus, ac bibendum nulla leo eu purus. Quisque nec diam sed risus consectetur accumsan quis quis nibh. Vestibulum id purus lorem.</p>
    </div>

    <div class="sign-off">Sincerely,</div>
    <div class="seal"></div>
    <div class="signature" role="img" aria-label="Handwritten signature"></div>

    <div class="footer">
      Address Line 1 Address Line 2<br>
      Tel: 123-555-984 Mob: 123-456-78 Fax: 123-456-78<br>
      yourname@sample.com&nbsp;&nbsp;www.yourcompany.com
    </div>
  </main>
</body>
</html>
```